Ozark Hollowpine Barbeque Sauce*

Design a branded label for a bottle of sauce..... for OZARK HOLLOWPINE BBQ
FOOD LABEL. Target audience is woman buying bbq sauce for men. There is a lot of competition in the market so Texas should really be a highlight. LOGO SHOULD BE BIG. PLEASE RECREATE IF YOU CAN.

I am looking for a unique die cut....

Target Market(s)

GENERAL GROCERY STORE

Industry/Entity Type

Retail

Colors
f58946
ec1f27
f78f20
fee18a
f48541

Requirements
Must have
• OZARK HOLLOWPINE BBQ SAUCE
Nice to have
• ILLUSTRATIONS
Should not have
• NO PICTURES BUT

```html
<!DOCTYPE html>
<html lang="en">
<head>
<meta charset="utf-8">
<title>Ozark Hollowpine Barbeque Sauce – Labels</title>
<link href="https://fonts.googleapis.com/css2?family=Rye&family=Ultra&family=Archivo+Narrow:wght@400;700&display=swap" rel="stylesheet">
<style>
  :root{
    --maroon:#8b0d22;
    --cream:#fcf1dc;
    --white:#ffffff;
    --ink:#1a1a1a;
    --flame-yellow:#fee18a;
    --flame-orange:#f78f20;
    --flame-red:#ec1f27;
    --stamp:#8b0d22;
  }
  *{box-sizing:border-box;margin:0;padding:0}
  html,body{width:1200px;height:1000px;overflow:hidden;background:var(--white)}
  .canvas{position:relative;width:1200px;height:1000px}
  .label{position:absolute;width:290px;height:795px;top:110px}
  .label--back{left:250px}
  .label--front{left:660px}
  .label__shape{position:absolute;inset:0}
  .label__content{position:absolute;inset:0}

  .brand-mark{position:absolute;left:50%;transform:translateX(-50%);border-radius:50%;
    background:radial-gradient(circle at 50% 60%,var(--flame-yellow) 0%,var(--flame-orange) 55%,var(--flame-red) 100%)}
  .brand-name{position:absolute;left:0;right:0;text-align:center;color:var(--cream);
    font-family:"Rye",serif;line-height:1}
  .label--front .brand-mark{top:70px;width:190px;height:190px}
  .label--front .brand-name{top:290px;font-size:30px}
  .label--front .brand-name span{display:block;font-size:19px;margin-top:8px}

  .product-name{position:absolute;left:0;right:0;text-align:center;color:var(--stamp);font-family:"Ultra",serif;line-height:1}
  .product-name--line1{top:500px;font-size:39px;letter-spacing:1px}
  .product-name--line2{top:588px;font-size:46px;letter-spacing:2px;display:flex;justify-content:center;align-items:center;gap:22px}
  .star{width:22px;height:22px;fill:var(--stamp)}

  .rule{position:absolute;left:60px;right:60px;height:1px;background:var(--cream)}
  .label--front .rule{top:705px}
  .volume{position:absolute;top:725px;left:0;right:0;text-align:center;color:var(--cream);font-family:"Rye",serif;font-size:16px}

  .label--back .brand-mark{top:40px;width:80px;height:80px}
  .label--back .brand-name{top:130px;font-size:16px}
  .label--back .brand-name span{display:block;font-size:10px;margin-top:3px}

  .nutrition{position:absolute;top:170px;left:27px;width:236px;background:var(--white);border:1px solid var(--ink);
    padding:4px 5px;font-family:"Archivo Narrow",sans-serif;color:var(--ink);font-size:9px;line-height:1.3}
  .nutrition__title{font-size:19px;font-weight:700;line-height:1}
  .nutrition__row{display:flex;justify-content:space-between;border-top:1px solid var(--ink)}
  .nutrition__row--thick{border-top:6px solid var(--ink)}
  .nutrition__row--mid{border-top:3px solid var(--ink)}
  .nutrition__cal{font-size:15px;font-weight:700;align-items:flex-end}
  .nutrition__cal b{font-size:22px}
  .indent{padding-left:10px}
  .indent2{padding-left:20px}
  .nutrition__foot{border-top:3px solid var(--ink);font-size:7px;line-height:1.25;padding-top:2px}
  .follow{position:absolute;top:664px;left:0;right:0;text-align:center;color:var(--cream);font-family:"Rye",serif;font-size:11px;
    display:flex;justify-content:center;align-items:center;gap:6px}
  .follow__dot{width:12px;height:12px;border-radius:50%;background:var(--cream)}
  .back-star{position:absolute;top:700px;left:50%;transform:translateX(-50%);width:24px;height:24px;fill:var(--cream)}
</style>
</head>
<body>
<main class="canvas">

  <section class="label label--back" aria-label="Back label">
    <svg class="label__shape" viewBox="0 0 290 795" width="290" height="795">
      <defs>
        <clipPath id="back-cut"><path d="M0,210 C0,170 20,150 45,135 C55,90 75,60 100,40 C115,25 130,10 145,0 C160,10 175,25 190,40 C215,60 235,90 245,135 C270,150 290,170 290,210 L290,650 A145,145 0 0 1 0,650 Z"/></clipPath>
      </defs>
      <path fill="var(--maroon)" d="M0,210 C0,170 20,150 45,135 C55,90 75,60 100,40 C115,25 130,10 145,0 C160,10 175,25 190,40 C215,60 235,90 245,135 C270,150 290,170 290,210 L290,650 A145,145 0 0 1 0,650 Z"/>
      <rect x="0" y="330" width="290" height="320" fill="var(--cream)" clip-path="url(#back-cut)"/>
      <path fill="none" stroke="var(--white)" stroke-width="1.5" transform="translate(8,8) scale(0.945,0.98)" d="M0,210 C0,170 20,150 45,135 C55,90 75,60 100,40 C115,25 130,10 145,0 C160,10 175,25 190,40 C215,60 235,90 245,135 C270,150 290,170 290,210 L290,650 A145,145 0 0 1 0,650 Z"/>
    </svg>
    <div class="label__content">
      <div class="brand-mark" role="img" aria-label="Brand mark area"></div>
      <div class="brand-name">OZARK<span>HOLLOWPINE BBQ</span></div>
      <div class="nutrition">
        <div class="nutrition__title">Nutrition Facts</div>
        <div>1 serving per container</div>
        <div class="nutrition__row" style="border-top:none"><span>Serving size</span><span>1/4 cup (40g)</span></div>
        <div class="nutrition__row nutrition__row--thick"><span>Amount per serving</span></div>
        <div class="nutrition__row nutrition__cal" style="border-top:none"><span>Calories</span><b>120</b></div>
        <div class="nutrition__row nutrition__row--mid"><span></span><span>% Daily Value*</span></div>
        <div class="nutrition__row"><span>Total Fat 0g</span><span>0 %</span></div>
        <div class="nutrition__row"><span class="indent">Saturated Fat 0g</span><span>0 %</span></div>
        <div class="nutrition__row"><span class="indent"><i>Trans</i> Fat 0g</span><span></span></div>
        <div class="nutrition__row"><span>Cholesterol 0mg</span><span>0 %</span></div>
        <div class="nutrition__row"><span>Sodium 10mg</span><span>0 %</span></div>
        <div class="nutrition__row"><span>Total Carbohydrate 32g</span><span>12 %</span></div>
        <div class="nutrition__row"><span class="indent">Dietary Fiber 2g</span><span>7 %</span></div>
        <div class="nutrition__row"><span class="indent">Total Sugars 26g</span><span></span></div>
        <div class="nutrition__row"><span class="indent2">Includes 0 Added Sugars</span><span>0 %</span></div>
        <div class="nutrition__row"><span>Protein 1g</span><span></span></div>
        <div class="nutrition__row nutrition__row--thick"><span>Vitamin D 0mcg</span><span>0 %</span></div>
        <div class="nutrition__row"><span>Calcium 25mg</span><span>2 %</span></div>
        <div class="nutrition__row"><span>Iron 0.7mg</span><span>4 %</span></div>
        <div class="nutrition__row"><span>Potassium 298mg</span><span>6 %</span></div>
        <div class="nutrition__foot">* Percent Daily Value shows how much a nutrient in one serving adds to a daily diet of 2,000 calories.<br><b>Ingredients: Sun-Dried Raisins</b></div>
      </div>
      <div class="follow">FOLLOW US ON <span class="follow__dot"></span></div>
      <svg class="back-star" viewBox="0 0 24 24"><polygon points="12,1 15,9 23,9 16.5,14 19,22 12,17 5,22 7.5,14 1,9 9,9"/></svg>
    </div>
  </section>

  <section class="label label--front" aria-label="Front label">
    <svg class="label__shape" viewBox="0 0 290 795" width="290" height="795">
      <defs>
        <clipPath id="front-cut"><path d="M0,210 C0,170 20,150 45,135 C55,90 75,60 100,40 C115,25 130,10 145,0 C160,10 175,25 190,40 C215,60 235,90 245,135 C270,150 290,170 290,210 L290,650 A145,145 0 0 1 0,650 Z"/></clipPath>
      </defs>
      <path fill="var(--maroon)" d="M0,210 C0,170 20,150 45,135 C55,90 75,60 100,40 C115,25 130,10 145,0 C160,10 175,25 190,40 C215,60 235,90 245,135 C270,150 290,170 290,210 L290,650 A145,145 0 0 1 0,650 Z"/>
      <rect x="0" y="465" width="290" height="215" fill="var(--cream)" clip-path="url(#front-cut)"/>
      <path fill="none" stroke="var(--white)" stroke-width="1.5" transform="translate(8,8) scale(0.945,0.98)" d="M0,210 C0,170 20,150 45,135 C55,90 75,60 100,40 C115,25 130,10 145,0 C160,10 175,25 190,40 C215,60 235,90 245,135 C270,150 290,170 290,210 L290,650 A145,145 0 0 1 0,650 Z"/>
    </svg>
    <div class="label__content">
      <div class="brand-mark" role="img" aria-label="Brand mark area"></div>
      <div class="brand-name">OZARK<span>HOLLOWPINE BBQ</span></div>
      <div class="product-name product-name--line1">BARBEQUE</div>
      <div class="product-name product-name--line2">
        <svg class="star" viewBox="0 0 24 24"><polygon points="12,1 15,9 23,9 16.5,14 19,22 12,17 5,22 7.5,14 1,9 9,9"/></svg>
        SAUCE
        <svg class="star" viewBox="0 0 24 24"><polygon points="12,1 15,9 23,9 16.5,14 19,22 12,17 5,22 7.5,14 1,9 9,9"/></svg>
      </div>
      <div class="rule"></div>
      <div class="volume">250ml</div>
    </div>
  </section>

</main>
</body>
</html>
```